Business Card and Letterhead for Vantel Psychology

We need a business card design and letterhead to use for our Psychology firm that specializes in psychoeducational assessments and individual therapy. Our motto is Purpose-Driven Assessments, Meaning-Centered Therapy.Our contact information is as follows:
Vantel Psychology
The Bramwick Block - 4127-38St.
Box 6154 Olds, AB
T2K 3R8
t 403.555.0148 (VANT)
f 403.555.0193
www.vantelpsych-example.ca
The business card will be used for two different psychologists so I can supply names nearer to completion. We prefer clean, uncluttered looks.

Target Market(s)

Clients, Educators

Font styles to use
Sans Serif

Colors

Designer to choose colors to be used in the design.

Requirements
Must have
• All relevant contact info, logo, some "white" space.
Nice to have
• It would be nice to see letterhead options that have the logo on the top of the page but also options that have it on the side. I think top of the page is probably our preference.
Should not have
• Too much clutter!

```html
<!DOCTYPE html>
<html lang="en">
<head>
<meta charset="utf-8">
<title>Vantel Psychology Letterhead</title>
<link rel="stylesheet" href="https://fonts.googleapis.com/css2?family=Questrial&family=Carlito&display=swap">
<style>
:root{
  --bg:#8ac6ef;
  --paper:#ffffff;
  --orange:#f08a32;
  --blue:#4fb6d6;
  --ink:#2b2b2b;
  --rule:#1a1a1a;
}
*{margin:0;padding:0;box-sizing:border-box}
html,body{width:1200px;height:898px;overflow:hidden;background:var(--bg)}
.letterhead{
  position:absolute;left:280px;top:34px;width:640px;height:830px;
  background:var(--paper);font-family:"Questrial",sans-serif;color:var(--ink);
  box-shadow:0 10px 30px rgba(0,40,80,.25);overflow:hidden;
}
.band{position:absolute;left:0;width:100%;height:12px}
.band--top{top:0}
.band--bottom{bottom:0}
.brand{position:absolute;left:60px;top:116px}
.brand__name{font-size:20px;color:var(--ink);font-weight:400}
.contact{position:absolute;right:40px;top:58px;text-align:right;font-family:"Carlito",sans-serif;font-size:11.5px;line-height:17px}
.contact__row{display:flex;justify-content:flex-end;align-items:center;gap:6px}
.contact__row svg{width:11px;height:11px}
.rule{position:absolute;left:60px;right:30px;top:148px;height:1.5px;background:var(--rule)}
.letter{position:absolute;left:70px;right:70px;top:200px;font-size:12px;line-height:19.5px}
.letter__greeting{font-size:14px;margin-bottom:18px}
.letter p{margin-bottom:26px;text-align:justify}
.signature{position:absolute;right:70px;top:600px;text-align:right}
.signature__name{font-size:16px}
.signature__title{font-size:10.5px;margin-top:3px}
.address{position:absolute;right:70px;bottom:40px;font-family:"Carlito",sans-serif;font-size:11px;letter-spacing:.3px}
</style>
</head>
<body>
<main class="letterhead">
  <svg class="band band--top" viewBox="0 0 640 12" preserveAspectRatio="none">
    <polygon points="0,0 300,0 294,12 0,12" fill="var(--orange)"/>
    <polygon points="304,0 640,0 640,12 298,12" fill="var(--blue)"/>
  </svg>

  <div class="brand">
    <span class="brand__name">Vantel Psychology</span>
  </div>

  <div class="contact">
    <div class="contact__row">403.555.0148
      <svg viewBox="0 0 12 12"><path d="M1 4 Q6 0 11 4 L9 6 L8 4 H4 L3 6 Z M3 6 H9 V11 H3 Z" fill="var(--blue)"/></svg></div>
    <div class="contact__row">403.555.0193
      <svg viewBox="0 0 12 12"><path d="M1 4 Q6 0 11 4 L9 6 L8 4 H4 L3 6 Z M3 6 H9 V11 H3 Z" fill="var(--blue)"/></svg></div>
    <div class="contact__row">reception@vantelpsych-example.ca
      <svg viewBox="0 0 12 12"><rect x="0.5" y="2.5" width="11" height="7" fill="var(--blue)"/><path d="M0.5 2.5 L6 7 L11.5 2.5" stroke="#fff" fill="none"/></svg></div>
    <div class="contact__row">www.vantelpsych-example.ca
      <svg viewBox="0 0 12 12"><circle cx="6" cy="6" r="5" fill="none" stroke="var(--blue)"/><path d="M1 6 H11 M6 1 V11" stroke="var(--blue)"/></svg></div>
  </div>

  <div class="rule"></div>

  <section class="letter">
    <div class="letter__greeting">Hello Sir/Mam</div>
    <p>Lorem ipsum dolor sit amet, consectetur adipiscing elit. Donec orci purus, luctus vitae dignissim eu, iaculis sed purus. Vivamus faucibus, ipsum nec aliquet viverra, leo mauris condimentum ligula, sit afefefefefemet sagittis enim ligula quis arcu. Nam egestas tortor id nisi porttitor mattis. In tortor ante, ultricies in suscsddddsdsd-sipit a, tempus non massa. Vivamus et auctor mi. Fuefefemhmhmhsce vel massa nulla. Phasedddllus nec eros mauris, et scelerisque orci. Dondddec malesuada orci vitae nulla accumsan porta a id massa.</p>
    <p>Quisque accumsan iaculis magna sit amet fringilla. Maefefeefefecenas consequat, magna eget tincidunt semper, odio nibh rutsdsdccccsdrum mi, id feugiat ante nisi eu risus. Vestibulum nunc orci, rhoncus a placerat in, ultricies in mi. Cras mattis vassdsdsrius eros, vel fringilla nisi suscipit eget. Quisque fefeefefeefefes-celzzzzzerisque sagittis nulla at porttitor. Maurfeefefeis a justo et tellus intefefefefe-fefefrdum tristique. Sed id augue vitae urna euismod comsdsdsdmodo aliquet a quam. Pellentesque arcu velit, cuzzzzrsus et malesuada ut, consequat et diam. Nullazzzzereefem erat sem, rhoncfefefefus id ullamcorper vitae, rhoncus et arcu. In ultrisdsdsdcies ultricies nulla.</p>
  </section>

  <div class="signature">
    <div class="signature__name">Owen Harlow</div>
    <div class="signature__title">Co-Founder &amp; CEO</div>
  </div>

  <div class="address">The Bramwick Block - 4127-38St. Box 6154 Olds, AB T2K 3R8</div>

  <svg class="band band--bottom" viewBox="0 0 640 12" preserveAspectRatio="none">
    <polygon points="0,0 400,0 394,12 0,12" fill="var(--blue)"/>
    <polygon points="404,0 640,0 640,12 398,12" fill="var(--orange)"/>
  </svg>
</main>
</body>
</html>
```